Creative Web Site to Sell Geology Classes for Homeschooling

I am starting a business to sell a variety of geology classes for homeschoolers. I am targeting classes for kids with dyslexia, although others will benefit as well. The classes will be delivered by mail. Each class will have a video, a manual, and rock samples. I need a landing page that I can link over to seven other pages, a page with a template for products, and a template of the pages that will not have products. All should be easy to edit. All pages should display well with handheld devices (phones), as well as desktops.

Designs look the same

```html
<!DOCTYPE html>
<html lang="en">
<head>
<meta charset="utf-8">
<title>Stone Trail Academy – Geology Classes</title>
<link href="https://fonts.googleapis.com/css2?family=Poppins:ital,wght@0,300;0,400;0,500;0,600;0,700;1,300;1,400&display=swap" rel="stylesheet">
<style>
:root{
  --coral:#f2675a;
  --mint:#6fd6b8;
  --mint-soft:#e2f8f0;
  --mint-pale:#effbf6;
  --purple:#6a5b8c;
  --ink:#1f1d2b;
  --text:#55535f;
  --muted:#9a98a3;
  --grey-band:#efefef;
  --footer:#2b2639;
  --white:#ffffff;
}
*{box-sizing:border-box;margin:0;padding:0}
html,body{width:1200px;height:4063px;overflow:hidden}
body{font-family:'Poppins',sans-serif;color:var(--text);background:var(--white);position:relative}
.abs{position:absolute}
a{text-decoration:none;color:inherit}

/* header */
.site-header{position:absolute;top:0;left:0;width:1200px;height:108px;z-index:3}
.brand{position:absolute;left:40px;top:30px;display:flex;align-items:center;gap:12px}
.brand-mark{width:44px;height:44px;border-radius:50%;background:var(--coral)}
.brand-name{font-size:20px;font-weight:700;color:var(--coral);line-height:1.05;width:120px}
.main-nav{position:absolute;left:298px;top:48px;display:flex;gap:34px;font-size:13px;color:var(--ink)}
.btn{display:inline-flex;align-items:center;justify-content:center;border-radius:4px;color:var(--white);font-size:10px;font-weight:600;letter-spacing:.5px;text-transform:uppercase}
.btn-login{position:absolute;left:921px;top:43px;width:110px;height:33px;background:var(--coral);gap:6px}
.btn-phone{position:absolute;left:1046px;top:43px;width:124px;height:33px;background:var(--mint);gap:6px}

/* hero */
.hero{position:absolute;top:0;left:0;width:1200px;height:660px}
.hero-bg{position:absolute;inset:0}
.hero-kicker{left:98px;top:222px;font-size:25px;font-weight:500;color:var(--ink)}
.hero-title{left:98px;top:248px;font-size:40px;font-weight:700;color:var(--coral);letter-spacing:.5px}
.hero-sub{left:98px;top:298px;width:380px;font-size:16px;line-height:1.4;color:var(--ink)}
.hero-sub b{font-weight:600}
.hero-search{left:98px;top:366px;width:302px;height:36px;background:var(--white);border-radius:3px;font-size:10px;color:var(--muted);padding:11px 14px;display:flex;align-items:center;gap:8px}
.btn-start{left:98px;top:412px;width:162px;height:34px;background:var(--mint)}
.laptop-body{left:550px;top:141px;width:565px;height:377px;background:#1c1b22;border-radius:14px 14px 4px 4px}
.laptop-screen{left:563px;top:154px;width:539px;height:356px;background:linear-gradient(135deg,#e7e3dc,#c9c2b6 55%,#b6ae9f)}
.laptop-base{left:488px;top:516px;width:677px;height:14px;background:linear-gradient(#d9d9dd,#9c9ca3);border-radius:0 0 60px 60px}

/* features */
.features{position:absolute;top:700px;left:0;width:1200px;display:flex;justify-content:center;gap:70px}
.feature{display:flex;gap:12px;align-items:flex-start;width:210px}
.feature svg{flex:none}
.feature h4{font-size:11px;font-weight:600;color:var(--ink)}
.feature p{font-size:9px;line-height:1.4;color:var(--text)}

/* about */
.about-photo-main{left:168px;top:861px;width:279px;height:385px;background:linear-gradient(135deg,#eef0ee,#d9cfc4 60%,#c8a88c);box-shadow:0 10px 30px rgba(0,0,0,.12)}
.about-photo-small{left:387px;top:1062px;width:214px;height:200px;background:linear-gradient(135deg,#c7cdd6,#7f8aa0 60%,#5b6580);border:6px solid var(--white);box-shadow:0 10px 30px rgba(0,0,0,.15)}
.accent-line{width:2px;height:34px;background:var(--coral)}
.eyebrow{font-size:15px;font-style:italic;font-weight:300;color:var(--ink)}
.section-title{font-size:40px;font-weight:700;color:var(--coral);letter-spacing:.5px}
.body-copy{font-size:11px;line-height:1.75;color:var(--text)}
.btn-purple{background:var(--purple);height:30px;width:114px;font-size:9px}

/* courses */
.courses{position:absolute;top:1382px;left:0;width:1200px;height:682px;background:var(--grey-band)}
.center{text-align:center;width:1200px;left:0}
.course-grid{position:absolute;left:168px;top:224px;display:flex;gap:11px}
.course-card{width:209px;height:298px;background:var(--white);position:relative;box-shadow:0 4px 14px rgba(0,0,0,.06)}
.course-img{height:155px;width:100%}
.avatar{position:absolute;right:12px;top:132px;width:44px;height:44px;border-radius:50%;background:#b8b0a6;border:3px solid var(--white)}
.course-meta{position:absolute;left:12px;top:168px;font-size:9px;color:var(--coral)}
.course-title{position:absolute;left:12px;top:182px;font-size:16px;font-weight:500;color:var(--ink)}
.course-text{position:absolute;left:12px;top:210px;width:170px;font-size:9.5px;line-height:1.5}
.course-foot{position:absolute;left:0;bottom:0;width:100%;height:40px;border-top:1px solid #ececec;display:flex;align-items:center;justify-content:space-between;padding-left:12px;font-size:9px;color:var(--muted)}
.course-foot .btn{height:40px;width:96px;border-radius:0;background:var(--mint);font-size:8.5px}
.btn-all{left:528px;top:568px;width:141px;height:33px}

/* feature split */
.split-photo{left:0;top:2067px;width:650px;height:588px;background:linear-gradient(160deg,#f4f4f4 30%,#e2e2e2 55%,#33577f 75%,#274a6e)}
.split-title{left:685px;top:2180px;width:380px;font-size:22px;font-weight:600;line-height:1.4;color:var(--ink)}
.split-copy{left:685px;top:2266px;width:350px}

/* news */
.news-grid{position:absolute;left:209px;top:2877px;display:flex;gap:16px}
.news-card{width:252px}
.news-img{height:171px}
.news-card h3{font-size:16px;font-weight:500;color:var(--ink);margin-top:22px}
.news-meta{font-size:9px;color:var(--muted);margin-top:6px}
.news-meta span{color:var(--coral)}
.read-more{display:inline-block;margin-top:22px;font-size:9px;font-weight:600;color:var(--ink);border-bottom:1px solid var(--ink)}

/* contact */
.contact{position:absolute;top:3243px;left:0;width:1200px;height:522px;background:var(--mint-soft)}
.contact-title{top:78px;font-size:25px;font-weight:500;color:var(--coral)}
.contact-sub{top:114px;font-size:10px;color:var(--ink)}
.field{position:absolute;height:35px;border:1px solid #c3e6d9;border-radius:3px;font-size:10px;color:var(--muted);padding:11px 14px;background:var(--mint-pale)}
.btn-submit{left:542px;top:409px;width:116px;height:28px;font-size:9px}

/* footer */
.site-footer{position:absolute;top:3765px;left:0;width:1200px;height:298px;background:var(--footer)}
.footer-brand{left:0;width:1200px;top:52px;display:flex;justify-content:center;align-items:center;gap:10px}
.footer-nav{left:0;width:1200px;top:143px;display:flex;justify-content:center;gap:60px;font-size:10px;color:#c7c3d3;text-transform:uppercase}
.footer-nav a:first-child{color:var(--white)}
.social{left:0;width:1200px;top:183px;display:flex;justify-content:center;gap:18px}
.social span{width:30px;height:30px;border:1px solid #6b6580;border-radius:50%}
.copyright{top:234px;font-size:10px;color:#c7c3d3}
</style>
</head>
<body>

<section class="hero">
  <svg class="hero-bg" width="1200" height="660" viewBox="0 0 1200 660" aria-hidden="true">
    <defs>
      <linearGradient id="heroFill" x1="0" y1="0" x2="1" y2="1">
        <stop offset="0" stop-color="#d9f6ec"/><stop offset="1" stop-color="#eefbf6"/>
      </linearGradient>
    </defs>
    <path d="M0 0H1200V400C1020 520 760 560 560 600C360 640 160 660 0 650Z" fill="url(#heroFill)"/>
  </svg>
  <p class="abs hero-kicker">Transform Your Home into a</p>
  <h1 class="abs hero-title">GEOLOGY CLASSES</h1>
  <p class="abs hero-sub"><b>Lorem Ipsum is</b> simply dummy text of the printing and typesetting</p>
  <div class="abs hero-search">
    <svg width="10" height="10" viewBox="0 0 10 10" aria-hidden="true"><circle cx="4" cy="4" r="3" fill="none" stroke="#9a98a3" stroke-width="1.2"/><path d="M6.3 6.3 9 9" stroke="#9a98a3" stroke-width="1.2"/></svg>
    Discover new experiments...
  </div>
  <a class="abs btn btn-start" href="#">Get Started Now!</a>
  <div class="abs laptop-body"></div>
  <div class="abs laptop-screen" role="img" aria-label="Photo of a parent reading with a child at home"></div>
  <div class="abs laptop-base"></div>
</section>

<header class="site-header">
  <div class="brand"><span class="brand-mark"></span><span class="brand-name">Stone Trail Academy</span></div>
  <nav class="main-nav"><a href="#">Home</a><a href="#">About</a><a href="#">Classes</a><a href="#">Product</a><a href="#">Blog</a><a href="#">Contact</a></nav>
  <a class="btn btn-login" href="#"><svg width="9" height="10" viewBox="0 0 9 10" aria-hidden="true"><rect x="1" y="4" width="7" height="6" rx="1" fill="#fff"/><path d="M2.5 4V2.8a2 2 0 0 1 4 0V4" fill="none" stroke="#fff"/></svg>Login Here</a>
  <a class="btn btn-phone" href="#"><svg width="10" height="10" viewBox="0 0 10 10" aria-hidden="true"><path d="M2 0.8 3.6 0.5 4.5 3 3.4 3.8C4 5.2 4.8 6 6.2 6.6L7 5.5 9.5 6.4 9.2 8C8.8 9.2 7.5 9.6 6.2 9 3.8 7.9 2.1 6.2 1 3.8.4 2.5.8 1.2 2 .8Z" fill="#fff"/></svg>555-014-2290</a>
</header>

<section class="features">
  <div class="feature">
    <svg width="34" height="30" viewBox="0 0 34 30" aria-hidden="true"><rect x="2" y="6" width="30" height="18" rx="2" fill="none" stroke="#f2675a" stroke-width="1.6"/><path d="M12 28h10M17 24v4" stroke="#f2675a" stroke-width="1.6"/></svg>
    <div><h4>Learn Anywhere</h4><p>Lorem ipsum is simply dummy text of the printing</p></div>
  </div>
  <div class="feature">
    <svg width="30" height="30" viewBox="0 0 30 30" aria-hidden="true"><circle cx="15" cy="15" r="12" fill="none" stroke="#f2675a" stroke-width="1.6"/><path d="M15 8v7l5 3" fill="none" stroke="#f2675a" stroke-width="1.6"/></svg>
    <div><h4>9000+ Activity</h4><p>Lorem ipsum is simply dummy text of the printing</p></div>
  </div>
  <div class="feature">
    <svg width="34" height="30" viewBox="0 0 34 30" aria-hidden="true"><circle cx="11" cy="10" r="5" fill="none" stroke="#f2675a" stroke-width="1.6"/><circle cx="24" cy="10" r="5" fill="none" stroke="#f2675a" stroke-width="1.6"/><path d="M2 27c1-6 5-9 9-9s8 3 9 9M16 22c2-3 4-4 8-4 4 0 8 3 9 9" fill="none" stroke="#f2675a" stroke-width="1.6"/></svg>
    <div><h4>24,000+ Students</h4><p>Lorem ipsum is simply dummy text of the printing</p></div>
  </div>
</section>

<section class="about">
  <div class="abs about-photo-main" role="img" aria-label="Photo of a tutor helping a child with schoolwork"></div>
  <div class="abs about-photo-small" role="img" aria-label="Photo of a child writing at a desk"></div>
  <div class="abs accent-line" style="left:691px;top:880px"></div>
  <p class="abs eyebrow" style="left:691px;top:912px">Lorem Ipsum is simply dummy text</p>
  <h2 class="abs section-title" style="left:691px;top:936px">ABOUT US</h2>
  <p class="abs body-copy" style="left:691px;top:1006px;width:350px">Lorem Ipsum is simply dummy text of the printing and typesetting industry. Lorem Ipsum has been the industry's standard dummy text ever since the 1500s, when an unknown printer took a galley of type and scrambled it to make a type specimen book. It has survived not only five centuries.</p>
  <p class="abs body-copy" style="left:691px;top:1116px;width:350px">But also the leap into electronic typesetting, remaining essentially unchanged. It was popularised in the 1960s with the release of Letraset sheets containing Lorem Ipsum passages.</p>
  <a class="abs btn btn-purple" style="left:691px;top:1205px" href="#">Read More</a>
</section>

<section class="courses">
  <div class="abs accent-line" style="left:599px;top:72px;height:28px"></div>
  <p class="abs eyebrow center" style="top:106px">Lorem Ipsum is simply dummy text</p>
  <h2 class="abs section-title center" style="top:130px">POPULAR COURSES</h2>
  <div class="course-grid">
    <article class="course-card">
      <div class="course-img" role="img" aria-label="Photo of a student writing" style="background:linear-gradient(135deg,#e9e4dc,#b9a58f)"></div>
      <span class="avatar"></span>
      <p class="course-meta">Teacher : Mara Quill</p>
      <h3 class="course-title">Lorem Ipsum is simple</h3>
      <p class="course-text">Lorem Ipsum is simply dummy text of the printing</p>
      <div class="course-foot">156 Students<a class="btn" href="#">Register Now</a></div>
    </article>
    <article class="course-card">
      <div class="course-img" role="img" aria-label="Photo of a student with glasses reading" style="background:linear-gradient(135deg,#d9dfe6,#7f93ad)"></div>
      <span class="avatar"></span>
      <p class="course-meta">Teacher : Mara Quill</p>
      <h3 class="course-title">Lorem Ipsum is simple</h3>
      <p class="course-text">Lorem Ipsum is simply dummy text of the printing</p>
      <div class="course-foot">156 Students<a class="btn" href="#">Register Now</a></div>
    </article>
    <article class="course-card">
      <div class="course-img" role="img" aria-label="Photo of a student studying at a table" style="background:linear-gradient(135deg,#c9ccd2,#5e6a7e)"></div>
      <span class="avatar"></span>
      <p class="course-meta">Teacher : Mara Quill</p>
      <h3 class="course-title">Lorem Ipsum is simple</h3>
      <p class="course-text">Lorem Ipsum is simply dummy text of the printing</p>
      <div class="course-foot">156 Students<a class="btn" href="#">Register Now</a></div>
    </article>
    <article class="course-card">
      <div class="course-img" role="img" aria-label="Photo of a child drawing on paper" style="background:linear-gradient(135deg,#ece6dd,#c4ab90)"></div>
      <span class="avatar"></span>
      <p class="course-meta">Teacher : Mara Quill</p>
      <h3 class="course-title">Lorem Ipsum is simple</h3>
      <p class="course-text">Lorem Ipsum is simply dummy text of the printing</p>
      <div class="course-foot">156 Students<a class="btn" href="#">Register Now</a></div>
    </article>
  </div>
  <a class="abs btn btn-purple btn-all" href="#">View All Courses</a>
</section>

<section class="split">
  <div class="abs split-photo" role="img" aria-label="Photo of a boy using a laptop in a white armchair"></div>
  <h2 class="abs split-title">Lorem Ipsum is simply dummy text of the printing</h2>
  <p class="abs body-copy split-copy">Lorem Ipsum is simply dummy text of the printing and typesetting industry. Lorem Ipsum has been the industry's standard dummy text ever since the 1500s, when an unknown printer took a galley of type and scrambled it to make a type specimen book. It has survived not only five centuries.</p>
  <a class="abs btn btn-purple" style="left:685px;top:2389px" href="#">Read More</a>
</section>

<section class="news">
  <p class="abs eyebrow center" style="top:2762px">Lorem Ipsum is simply dummy text</p>
  <h2 class="abs section-title center" style="top:2786px">NEWS POSTS</h2>
  <div class="news-grid">
    <article class="news-card">
      <div class="news-img" role="img" aria-label="Photo of wooden letter blocks" style="background:linear-gradient(135deg,#a69a86,#6f6555)"></div>
      <h3>Lorem Ipsum is simple dolor</h3>
      <p class="news-meta">By <span>Admin</span> | 18 February, 2018</p>
      <a class="read-more" href="#">READ MORE</a>
    </article>
    <article class="news-card">
      <div class="news-img" role="img" aria-label="Photo of students studying together" style="background:linear-gradient(135deg,#e8e2da,#b48f7a)"></div>
      <h3>Lorem Ipsum is simple dolor</h3>
      <p class="news-meta">By <span>Admin</span> | 18 February, 2018</p>
      <a class="read-more" href="#">READ MORE</a>
    </article>
    <article class="news-card">
      <div class="news-img" role="img" aria-label="Photo of a student writing in a classroom" style="background:linear-gradient(135deg,#cfd4da,#62708a)"></div>
      <h3>Lorem Ipsum is simple dolor</h3>
      <p class="news-meta">By <span>Admin</span> | 18 February, 2018</p>
      <a class="read-more" href="#">READ MORE</a>
    </article>
  </div>
</section>

<section class="contact">
  <h2 class="abs center contact-title">Talk with an Expert</h2>
  <p class="abs center contact-sub">Lorem Ipsum is simply dummy text of the printing and typesetting industry</p>
  <div class="field" style="left:282px;top:157px;width:311px">Your Name</div>
  <div class="field" style="left:607px;top:157px;width:311px">Email Address</div>
  <div class="field" style="left:282px;top:211px;width:311px">Phone Number</div>
  <div class="field" style="left:607px;top:211px;width:311px;display:flex;justify-content:space-between">Online Courses<svg width="8" height="5" viewBox="0 0 8 5" aria-hidden="true"><path d="M0 0l4 5 4-5" fill="#9a98a3"/></svg></div>
  <div class="field" style="left:282px;top:265px;width:636px;height:122px">Your Message</div>
  <a class="abs btn btn-purple btn-submit" href="#">Submit Here</a>
</section>

<footer class="site-footer">
  <div class="abs footer-brand"><span class="brand-mark"></span><span class="brand-name" style="width:auto">Stone Trail Academy</span></div>
  <nav class="abs footer-nav"><a href="#">Home</a><a href="#">About</a><a href="#">Classes</a><a href="#">Product</a><a href="#">Blog</a><a href="#">Contact</a></nav>
  <div class="abs social"><span></span><span></span><span></span><span></span></div>
  <p class="abs center copyright">© 2018 Stone Trail Academy. All rights reserved.</p>
</footer>

</body>
</html>
```